Building sign design

We need a sign design for the front of our automotive workshop building. The sign needs to fit the colours of our building and company. (black, red, grey and white). The sign needs to stand out and be a modern.

Sign is to replace the red Corvane Cells sign. 2900mmx2900mm.
Company logo attached (Fastlane).
Also photos of old sign and building.

Sign needs to feature Fastlane logo at top and what we do below.

-Warrant of Fitness
-Vehicle Servicing
-All Mechanical Repairs
-Tyres & Wheel Alignments
-Batteries & Diagnostics
-Automotive Parts
-Vehicle Sales.

Also needs a large "WOF" somewhere on sign.

And contact details at bottom of sign.
48 Tarlow Drive
07 392 4718

```html
<!DOCTYPE html>
<html lang="en">
<head>
<meta charset="utf-8">
<title>Fastlane – Building Sign</title>
<link rel="stylesheet" href="https://fonts.googleapis.com/css2?family=Anton&family=Krona+One&family=Saira+Condensed:ital,wght@1,800&display=swap">
<style>
  :root {
    --red: #e0242a;
    --red-dark: #b8191e;
    --black: #111111;
    --panel: #1c1c1d;
    --grey: #7b7b7d;
    --white: #ffffff;
    --page: #ffffff;
  }
  * { margin: 0; padding: 0; box-sizing: border-box; }
  html, body {
    width: 926px; height: 1200px; overflow: hidden; background: var(--page);
  }
  .canvas { position: relative; width: 926px; height: 1200px; }
  .sign {
    position: absolute; left: 22px; top: 159px;
    width: 1335px; height: 1335px;
    transform: scale(0.66); transform-origin: 0 0;
    background: var(--white);
    box-shadow: 0 4px 18px rgba(0,0,0,0.25);
  }
  .sign-art { position: absolute; inset: 0; }
  .brand-name {
    position: absolute; left: 0; right: 0; top: 100px;
    text-align: center;
    font-family: "Krona One", sans-serif;
    font-size: 96px; letter-spacing: 6px;
    color: var(--red);
  }
  .headline {
    position: absolute; left: 0; right: 0; top: 272px;
    text-align: center;
    font-family: "Anton", sans-serif;
    font-size: 200px; line-height: 1;
    color: var(--white);
  }
  .services { position: absolute; left: 247px; top: 0; list-style: none; }
  .services li {
    position: absolute; left: 0; white-space: nowrap;
    font-family: "Krona One", sans-serif;
    font-size: 38px; letter-spacing: 5px;
    color: var(--white);
    transform: translateY(-50%);
  }
  .contact {
    position: absolute; left: 50px; top: 1205px;
    font-family: "Saira Condensed", sans-serif;
    font-style: italic; font-weight: 800;
    font-size: 112px; line-height: 1;
    color: var(--black);
    white-space: nowrap;
  }
</style>
</head>
<body>
<div class="canvas">
  <div class="sign">
    <svg class="sign-art" viewBox="0 0 1335 1335" width="1335" height="1335">
      <defs>
        <radialGradient id="engine-tone" cx="0.55" cy="0.45" r="0.75">
          <stop offset="0" stop-color="#2b2b2c"/>
          <stop offset="1" stop-color="#141414"/>
        </radialGradient>
        <linearGradient id="red-fade" x1="0" y1="0" x2="1" y2="0">
          <stop offset="0" stop-color="#e0242a"/>
          <stop offset="1" stop-color="#c91c22"/>
        </linearGradient>
        <polygon id="hex" points="0,-44 40,-22 40,22 0,44 -40,22 -40,-22"/>
      </defs>

      <rect class="backdrop" x="15" y="15" width="1305" height="1180" fill="url(#engine-tone)" role="img" aria-label="Dark photograph of an engine bay with spanners"/>

      <polygon class="top-band-red" points="15,15 700,15 680,33 15,33" fill="var(--red)"/>
      <polygon class="top-band-grey" points="700,15 1320,15 1320,43 672,43 680,33" fill="var(--grey)"/>

      <g class="headline-stripes" fill="var(--red)">
        <polygon points="340,405 465,405 465,415 352,415"/>
        <polygon points="356,425 465,425 465,435 368,435"/>
        <polygon points="868,405 995,405 983,415 868,415"/>
        <polygon points="868,425 979,425 967,435 868,435"/>
      </g>

      <g class="service-markers">
        <g transform="translate(0,565)"><rect x="15" y="-4" width="120" height="8" fill="var(--white)"/><use href="#hex" x="172" fill="var(--red)"/>
          <g stroke="var(--white)" stroke-width="5" fill="none" stroke-linejoin="round"><rect x="154" y="-16" width="32" height="32" rx="3"/><polyline points="160,-2 170,8 192,-16"/></g></g>
        <g transform="translate(0,650)"><rect x="15" y="-4" width="120" height="8" fill="var(--white)"/><use href="#hex" x="172" fill="var(--red)"/>
          <g stroke="var(--white)" stroke-width="4" fill="none"><line x1="148" y1="-20" x2="148" y2="20"/><line x1="196" y1="-20" x2="196" y2="20"/><line x1="148" y1="16" x2="196" y2="16"/><path d="M156 8 V-2 L162 -12 H182 L188 -2 V8 Z" fill="var(--white)"/></g></g>
        <g transform="translate(0,732)"><rect x="15" y="-4" width="120" height="8" fill="var(--white)"/><use href="#hex" x="172" fill="var(--red)"/>
          <g stroke="var(--white)" stroke-width="6" stroke-linecap="round"><line x1="156" y1="-16" x2="188" y2="16"/><line x1="188" y1="-16" x2="156" y2="16"/></g></g>
        <g transform="translate(0,817)"><rect x="15" y="-4" width="120" height="8" fill="var(--white)"/><use href="#hex" x="172" fill="var(--red)"/>
          <g stroke="var(--white)" fill="none"><circle cx="176" cy="0" r="18" stroke-width="6"/><circle cx="176" cy="0" r="6" stroke-width="4"/><line x1="150" y1="-14" x2="160" y2="-14" stroke-width="4"/><line x1="150" y1="14" x2="160" y2="14" stroke-width="4"/></g></g>
        <g transform="translate(0,900)"><rect x="15" y="-4" width="120" height="8" fill="var(--white)"/><use href="#hex" x="172" fill="var(--red)"/>
          <g fill="var(--white)"><rect x="152" y="-12" width="40" height="26" rx="2"/><rect x="157" y="-18" width="7" height="6"/><rect x="180" y="-18" width="7" height="6"/><polygon points="174,-8 164,3 171,3 168,10 180,-1 173,-1" fill="var(--red)"/></g></g>
        <g transform="translate(0,985)"><rect x="15" y="-4" width="120" height="8" fill="var(--white)"/><use href="#hex" x="172" fill="var(--red)"/>
          <g stroke="var(--white)" fill="none"><circle cx="172" cy="0" r="20" stroke-width="6" stroke-dasharray="26 6"/><circle cx="172" cy="0" r="7" stroke-width="5"/></g></g>
        <g transform="translate(0,1067)"><rect x="15" y="-4" width="120" height="8" fill="var(--white)"/><use href="#hex" x="172" fill="var(--red)"/>
          <g fill="var(--white)"><circle cx="166" cy="-8" r="12"/><rect x="152" y="4" width="42" height="12" rx="2"/><rect x="178" y="-4" width="14" height="10"/><circle cx="160" cy="18" r="5"/><circle cx="186" cy="18" r="5"/></g>
          <text x="166" y="-3" font-family="Krona One, sans-serif" font-size="13" text-anchor="middle" fill="var(--red)">$</text></g>
      </g>

      <polygon class="bottom-accent" points="1065,1147 1160,1045 1320,1045 1320,1147" fill="url(#red-fade)"/>
      <polygon class="bottom-band-red" points="595,1195 635,1147 1320,1147 1320,1195" fill="url(#red-fade)"/>
      <polygon class="bottom-band-grey" points="15,1160 623,1160 595,1195 15,1195" fill="var(--grey)"/>
      <polygon class="contact-wedge" points="1155,1195 1320,1195 1320,1320 1250,1320" fill="var(--red)"/>
    </svg>

    <div class="brand-name">FASTLANE</div>
    <div class="headline">WOF</div>

    <ul class="services">
      <li style="top:565px">Warrant of Fitness</li>
      <li style="top:650px">Vehicle Servicing</li>
      <li style="top:732px">All Mechanical Repairs</li>
      <li style="top:817px">Tyres &amp; Wheel Alignments</li>
      <li style="top:900px">Batteries &amp; Diagnostics</li>
      <li style="top:985px">Automotive Parts</li>
      <li style="top:1067px">Vehicle Sales</li>
    </ul>

    <div class="contact">48 Tarlow Drive | 07 392 4718</div>
  </div>
</div>
</body>
</html>
```